Wordpress Design for my Consulting Company

We want a WordPress site created for our new business. We have created a mock-up of the content we want on the site at https://marcusdellow.example-sites.com/website-5

We are not attached to any of the pictures and just put stock stuff from wix's editor, which we don't have rights to use outside of wix.

We are NOT looking to just port this site to WordPress, we are looking for some creative ways to display the content in a more professional artistic sense.

I have included several logo files and a text file with the colors and Fonts used in the logo. We are not looking to change the logo or the colors used in the logo.

The Schedule appointment links to a page that embeds a bookingnest.example.com calendar. https://bookingnest.example.com/marcus-dellow/brightvale

The final website domain will be enterprisebrightvale.example

Enterprise brightvale is a consulting company that works directly with the business owners and leaders of small businesses between 50-200 employees. We help companies make sure they have the right technology to meet their strategic goals. We are the anti-"Computer Guy" and we focus on business outcomes NOT cool technology gadgets.

The final design should communicate business growth and success.

Target Market(s)

Business Owners of companies with 50-200 employees

Coding

Coded - Design and coding required

Number of Pages Required

1 page

Font styles to use
Serif
Other font styles liked:
• Trajan Pro Bold, Open Sans

Requirements
Must have
• Should focus on consulting rather than technology.
• Should show the customer as the hero and we are just their guide.
• Must use the logo provided and the colors and fonts in the text file provided. Any other colors and fonts must be complementary.
• The design should scale for all devices computer, iPad, or phone
Should not have
• Should not focus on technology, we are the anti-"Computer Guy" and we focus on business outcomes NOT cool technology gadgets.

```html
<!DOCTYPE html>
<html lang="en">
<head>
<meta charset="utf-8">
<title>Brightvale — Technology Advisors That Get Business</title>
<link rel="stylesheet" href="https://fonts.googleapis.com/css2?family=Cinzel:wght@400;700&family=Open+Sans:wght@400;600;700&display=swap">
<style>
:root{
  --copper:#c67a4b;
  --copper-dark:#a9623a;
  --navy:#2d3e4f;
  --slate:#4d5c69;
  --slate-light:#6b7a86;
  --ink:#2b2b2b;
  --charcoal:#232323;
  --card:#f4f4f4;
  --white:#ffffff;
  --muted:#d7dde2;
}
*{margin:0;padding:0;box-sizing:border-box}
html,body{width:1200px;height:5279px;overflow:hidden}
body{font-family:"Open Sans",Arial,sans-serif;color:var(--ink);background:var(--white);position:relative}
.serif{font-family:"Cinzel",Georgia,serif}
section,header,footer{position:absolute;left:0;width:1200px}
.btn{display:inline-block;background:var(--copper);color:var(--white);font-family:"Cinzel",Georgia,serif;font-size:19px;letter-spacing:1px;padding:14px 26px;text-decoration:none;box-shadow:0 3px 6px rgba(0,0,0,.25)}
.center{text-align:center}

/* Hero */
.hero{top:0;height:950px;background:linear-gradient(160deg,#e9eef2 0%,#c5ced6 35%,#8b99a5 62%,#57636e 100%)}
.hero-photo{position:absolute;inset:0 0 280px 0;background:linear-gradient(170deg,rgba(255,255,255,.55),rgba(120,135,150,.35) 60%,rgba(60,70,80,.6))}
.brand{position:absolute;left:42px;top:58px;display:flex;align-items:center;gap:16px}
.brand-dot{width:70px;height:70px;border-radius:50%;background:var(--copper)}
.brand-name{font-family:"Cinzel",Georgia,serif;font-weight:700;font-size:30px;color:var(--navy);letter-spacing:1px}
.top-links{position:absolute;right:42px;top:100px;display:flex;gap:32px;font-family:"Cinzel",Georgia,serif;font-size:17px;color:var(--navy)}
.top-links span{display:flex;align-items:center;gap:8px}
.hero-title{position:absolute;top:300px;width:100%;text-align:center;font-family:"Cinzel",Georgia,serif;font-weight:700;font-size:42px;color:var(--navy);letter-spacing:1.5px}
.hero-cta{position:absolute;top:362px;width:100%;text-align:center}
.hero-band{position:absolute;left:0;bottom:0;width:100%;height:290px;background:var(--charcoal)}
.hero-band svg{position:absolute;top:-40px;left:0}
.hero-band p{position:absolute;top:95px;left:90px;right:90px;text-align:center;color:var(--white);font-size:23px;line-height:1.55}

/* What we do */
.services{top:950px;height:730px}
.section-title{font-family:"Cinzel",Georgia,serif;font-weight:700;font-size:30px;color:var(--navy);letter-spacing:1px;text-align:center}
.section-title em{font-style:normal;color:var(--copper)}
.services .section-title{margin-top:108px}
.service-grid{position:absolute;top:187px;left:95px;display:grid;grid-template-columns:repeat(3,305px);column-gap:40px;row-gap:63px}
.service-card{height:203px;background:var(--card);display:flex;flex-direction:column;align-items:center;justify-content:center;gap:18px;text-align:center;font-weight:700;font-size:17px;color:var(--ink);line-height:1.35}

/* Tired */
.tired{top:1680px;height:573px;background:linear-gradient(180deg,#4d5c69,#404e5a)}
.tired .section-title{color:var(--white);padding-top:85px}
.tired-list{position:absolute;top:180px;left:95px;display:grid;grid-template-columns:500px 460px;column-gap:45px;row-gap:22px;list-style:none}
.tired-list li{display:flex;gap:12px;color:var(--white);font-weight:700;font-size:16px;line-height:1.35}
.tired-list li::before{content:"";flex:none;width:14px;height:14px;margin-top:3px;border-radius:3px;background:#e0554a}
.tired-cta{position:absolute;top:420px;width:100%;text-align:center}
.curve{position:absolute;left:0;width:1200px}

/* Frustration */
.frustration{top:2253px;height:907px}
.photo-circle{position:absolute;top:158px;width:317px;height:317px;border-radius:50%}
.photo-a{left:160px;background:linear-gradient(140deg,#e4e8ec,#9fb0bf 55%,#5b6b7a)}
.photo-b{left:620px;background:linear-gradient(140deg,#eef1f4,#b8c4cf 50%,#6d7d8b)}
.frustration p{position:absolute;top:497px;width:420px;text-align:center;font-size:20px;line-height:1.5;color:var(--ink)}
.frustration .col-a{left:110px}
.frustration .col-b{left:570px}
.frustration-cta{position:absolute;top:773px;width:100%;text-align:center}

/* Testimonial */
.testimonial{top:3160px;height:500px;background:linear-gradient(180deg,#56646f,#44515c)}
.testimonial blockquote{position:absolute;top:110px;left:110px;right:110px;text-align:center;color:var(--white);font-size:21px;line-height:1.55}
.author{position:absolute;top:238px;left:0;width:100%;display:flex;justify-content:center;align-items:center;gap:20px}
.avatar{width:110px;height:110px;border-radius:50%;background:linear-gradient(150deg,#b69b86,#6e5a4e);border:3px solid var(--white)}
.author span{font-family:"Cinzel",Georgia,serif;font-size:22px;color:var(--white);letter-spacing:1px}
.dots{position:absolute;top:386px;width:100%;display:flex;justify-content:center;gap:7px}
.dots i{width:18px;height:18px;border-radius:50%;border:2px solid var(--white)}
.dots i.on{background:var(--copper);border-color:var(--copper)}

/* Steps */
.steps{top:3660px;height:740px}
.steps .section-title{margin-top:165px;font-size:27px}
.step-row{position:absolute;top:268px;left:95px;width:1010px;display:grid;grid-template-columns:repeat(4,1fr);column-gap:30px}
.step{text-align:center}
.step-icon{width:86px;height:86px;margin:0 auto 18px;border-radius:50%;background:var(--slate);display:flex;align-items:center;justify-content:center}
.step h3{font-family:"Cinzel",Georgia,serif;font-weight:400;font-size:22px;color:var(--navy);margin-bottom:6px}
.step p{font-size:15px;font-weight:700;line-height:1.4}
.step-arrow{position:absolute;top:22px}
.steps-cta{position:absolute;top:582px;width:100%;text-align:center}

/* Contact */
.contact{top:4400px;height:560px;background:linear-gradient(180deg,#505e6a,#3c4955)}
.contact h2{position:absolute;top:90px;font-family:"Cinzel",Georgia,serif;font-weight:700;font-size:30px;color:var(--white);letter-spacing:1px}
.contact .msg-title{left:95px}
.contact .info-title{left:762px}
.form{position:absolute;top:168px;left:95px;width:578px}
.form-row{display:grid;grid-template-columns:repeat(3,1fr);gap:8px;margin-bottom:8px}
.field{background:#2f3a44;color:var(--white);font-weight:700;font-size:15px;padding:14px 12px;height:52px}
.field.area{height:118px}
.submit{display:inline-block;margin-top:14px;background:var(--copper);color:var(--white);font-weight:700;font-size:18px;width:214px;text-align:center;padding:12px 0}
.info{position:absolute;top:168px;left:762px;width:360px;color:var(--white);font-weight:700;font-size:16px;line-height:1.4}
.info div{display:flex;gap:12px;margin-bottom:22px}
.info svg{flex:none;margin-top:2px}

/* Footer */
.footer{top:4928px;height:317px;background:var(--charcoal)}
.footer-brand{position:absolute;top:92px;width:100%;display:flex;justify-content:center;align-items:center;gap:16px}
.footer-brand .brand-name{color:var(--white)}
.footer-links{position:absolute;top:240px;width:100%;display:flex;justify-content:center;gap:32px;font-family:"Cinzel",Georgia,serif;font-size:17px;color:var(--white)}
.footer-links span{display:flex;align-items:center;gap:8px}
.copyright{top:5245px;height:34px;background:var(--white);text-align:center;font-size:11px;line-height:34px;color:#555;letter-spacing:.5px}
</style>
</head>
<body>

<header class="hero">
  <div class="hero-photo" role="img" aria-label="Businessperson in a suit touching a rising growth arrow above a city skyline"></div>
  <div class="brand"><span class="brand-dot"></span><span class="brand-name">BRIGHTVALE</span></div>
  <nav class="top-links">
    <span><svg width="20" height="18" viewBox="0 0 20 18"><rect x="1" y="3" width="18" height="14" fill="none" stroke="#c67a4b" stroke-width="2"/><path d="M1 7h18M6 1v4M14 1v4" stroke="#c67a4b" stroke-width="2"/></svg>Schedule Appointment</span>
    <span><svg width="18" height="18" viewBox="0 0 24 24"><path d="M6.6 10.8a15 15 0 0 0 6.6 6.6l2.2-2.2a1 1 0 0 1 1-.25 11 11 0 0 0 3.6.6 1 1 0 0 1 1 1V20a1 1 0 0 1-1 1A17 17 0 0 1 3 4a1 1 0 0 1 1-1h3.5a1 1 0 0 1 1 1 11 11 0 0 0 .6 3.6 1 1 0 0 1-.25 1z" fill="#c67a4b"/></svg>Contact Us</span>
  </nav>
  <h1 class="hero-title">TECHNOLOGY ADVISORS THAT "GET" BUSINESS</h1>
  <div class="hero-cta"><a class="btn" href="#">SCHEDULE APPOINTMENT</a></div>
  <div class="hero-band">
    <svg width="1200" height="80" viewBox="0 0 1200 80" preserveAspectRatio="none"><path d="M0 40 Q600 80 1200 20 L1200 80 L0 80Z" fill="#232323"/><path d="M0 40 Q600 80 1200 20" fill="none" stroke="#c67a4b" stroke-width="5"/></svg>
    <p>Enterprise brightvale is a consulting company that works directly with the business owners and leaders of small businesses between 50-200 employees. We help companies make sure they have the right technology to meet their strategic goals. We are the anti-"Computer Guy" and we focus on business outcomes NOT cool technology gadgets.</p>
  </div>
</header>

<section class="services">
  <h2 class="section-title">WHAT <em>BRIGHTVALE</em> DOES</h2>
  <div class="service-grid">
    <div class="service-card">
      <svg width="58" height="58" viewBox="0 0 58 58"><circle cx="30" cy="30" r="22" fill="none" stroke="#2d3e4f" stroke-width="5"/><path d="M30 18v13l9 6" fill="none" stroke="#2d3e4f" stroke-width="5"/><path d="M4 16l6 10 8-7" fill="none" stroke="#c67a4b" stroke-width="4"/></svg>
      We get reducing time<br>to decision</div>
    <div class="service-card">
      <svg width="60" height="58" viewBox="0 0 60 58"><rect x="6" y="38" width="8" height="18" fill="#c67a4b"/><rect x="20" y="30" width="8" height="26" fill="#c67a4b"/><rect x="34" y="22" width="8" height="34" fill="#c67a4b"/><rect x="48" y="14" width="8" height="42" fill="#c67a4b"/><path d="M18 6h6M21 3v6M30 4h5M32.5 1.5v5" stroke="#c67a4b" stroke-width="2"/></svg>
      We get leverage</div>
    <div class="service-card">
      <svg width="70" height="60" viewBox="0 0 70 60"><circle cx="35" cy="30" r="8" fill="#2d3e4f"/><path d="M21 56a14 12 0 0 1 28 0z" fill="#2d3e4f"/><g fill="#c67a4b"><circle cx="12" cy="22" r="4"/><circle cx="22" cy="10" r="4"/><circle cx="35" cy="5" r="4"/><circle cx="48" cy="10" r="4"/><circle cx="58" cy="22" r="4"/></g></svg>
      We get standardizing<br>customer experience</div>
    <div class="service-card">
      <svg width="58" height="58" viewBox="0 0 58 58"><path d="M8 50L50 8M32 8h18v18M8 32v18h18" fill="none" stroke="#c67a4b" stroke-width="5"/></svg>
      We get scaling up</div>
    <div class="service-card">
      <svg width="52" height="62" viewBox="0 0 52 62"><rect x="4" y="6" width="44" height="52" rx="4" fill="none" stroke="#2d3e4f" stroke-width="4"/><path d="M14 20l5 5 8-9M14 40l10 8M24 40l-10 8" fill="none" stroke="#c67a4b" stroke-width="3.5"/><path d="M32 22h8M32 44h8" stroke="#2d3e4f" stroke-width="3"/></svg>
      We get eliminating<br>bottlenecks</div>
    <div class="service-card">
      <svg width="52" height="60" viewBox="0 0 52 60"><path d="M26 3L4 11v18c0 14 10 24 22 28 12-4 22-14 22-28V11z" fill="none" stroke="#2d3e4f" stroke-width="4"/><path d="M16 30l7 7 13-14" fill="none" stroke="#c67a4b" stroke-width="4"/></svg>
      We get preparing<br>for disruption</div>
  </div>
</section>

<section class="tired">
  <h2 class="section-title">ARE YOU TIRED OF "COMPUTER GUYS" THAT...</h2>
  <ul class="tired-list">
    <li>Don't want to be involved in business strategy.</li>
    <li>Give you the excuse, "You never asked."</li>
    <li>Say "No!" but do not give options on how to achieve your business outcome.</li>
    <li>Recommend technology when a simple process or policy change would have the same effect.</li>
    <li>Can't explain how a technology will create business value, but insist it is necessary.</li>
    <li>Suggest expensive solutions that are just thrown away, soon after they are deployed.</li>
  </ul>
  <div class="tired-cta"><a class="btn" href="#">SCHEDULE APPOINTMENT</a></div>
  <svg class="curve" style="bottom:-1px" width="1200" height="60" viewBox="0 0 1200 60" preserveAspectRatio="none"><path d="M0 20 Q600 60 1200 20 L1200 60 L0 60Z" fill="#fff"/><path d="M0 20 Q600 60 1200 20" fill="none" stroke="#c67a4b" stroke-width="5"/></svg>
</section>

<section class="frustration">
  <div class="photo-circle photo-a" role="img" aria-label="Frustrated office team gathered around a computer"></div>
  <div class="photo-circle photo-b" role="img" aria-label="Hands reviewing charts on a tablet at a desk"></div>
  <p class="col-a">We get the frustration of working with consultants and experts who don't listen or take the time to understand your company goals and vision. We believe technology should serve your business, not the other way around.</p>
  <p class="col-b">Computer guys frustrate business leaders because they don't have a business mindset. Brightvale advises on strategy that helps companies apply technology to gain a competitive advantage.</p>
  <div class="frustration-cta"><a class="btn" href="#">SCHEDULE APPOINTMENT</a></div>
</section>

<section class="testimonial">
  <svg class="curve" style="top:-1px" width="1200" height="50" viewBox="0 0 1200 50" preserveAspectRatio="none"><path d="M0 0 L1200 0 L1200 10 Q600 50 0 10Z" fill="#fff"/></svg>
  <blockquote>"I knew I was behind, I just didn't know by how much. We had years of band-aided solutions and Brightvale helped us stabilize our environment and position ourselves to compete in the quickly changing world of copy and print"</blockquote>
  <div class="author"><div class="avatar" role="img" aria-label="Portrait of the client"></div><span>- Dana Whitlock, Print Harbor -</span></div>
  <div class="dots"><i class="on"></i><i></i><i></i><i></i><i></i></div>
  <svg class="curve" style="bottom:-1px" width="1200" height="60" viewBox="0 0 1200 60" preserveAspectRatio="none"><path d="M0 20 Q600 60 1200 20 L1200 60 L0 60Z" fill="#fff"/><path d="M0 20 Q600 60 1200 20" fill="none" stroke="#c67a4b" stroke-width="5"/></svg>
</section>

<section class="steps">
  <h2 class="section-title">THE 4 STEPS TO ALIGNING TECHNOLOGY <em>TO YOUR BUSINESS STRATEGY!</em></h2>
  <div class="step-row">
    <div class="step">
      <div class="step-icon"><svg width="40" height="40" viewBox="0 0 40 40"><circle cx="16" cy="16" r="11" fill="none" stroke="#fff" stroke-width="4"/><path d="M24 24l12 12" stroke="#fff" stroke-width="5"/></svg></div>
      <h3>01. Discover</h3><p>Identify what is going on behind the scenes, and create a snapshot of the current infrastructure.</p></div>
    <div class="step">
      <div class="step-icon"><svg width="40" height="40" viewBox="0 0 40 40"><path d="M4 8h4M4 20h4M4 32h4M14 8h22M14 20h16M14 32h20" stroke="#fff" stroke-width="4"/></svg></div>
      <h3>02. Prioritize</h3><p>Meet to decide which solutions and policies will have the greatest impact on reaching the companies goals.</p></div>
    <div class="step">
      <div class="step-icon"><svg width="42" height="42" viewBox="0 0 42 42"><circle cx="21" cy="21" r="7" fill="none" stroke="#fff" stroke-width="4"/><path d="M21 3v7M21 32v7M3 21h7M32 21h7M8 8l5 5M29 29l5 5M34 8l-5 5M13 29l-5 5" stroke="#fff" stroke-width="4"/></svg></div>
      <h3>03. Implement</h3><p>Implement those things that will give the greatest return on investment.</p></div>
    <div class="step">
      <div class="step-icon"><svg width="40" height="40" viewBox="0 0 40 40"><path d="M6 34L30 10M26 6l8 8M34 34L10 10M6 6l6 6" stroke="#fff" stroke-width="4.5"/></svg></div>
      <h3>04. Maintain</h3><p>Create a system that keeps your technology aligned as strategy adjusts over time.</p></div>
    <svg class="step-arrow" style="left:188px" width="84" height="30" viewBox="0 0 84 30"><path d="M2 18 Q42 -4 78 18M70 10l8 8-10 3" fill="none" stroke="#c67a4b" stroke-width="3"/></svg>
    <svg class="step-arrow" style="left:448px" width="84" height="30" viewBox="0 0 84 30"><path d="M2 18 Q42 -4 78 18M70 10l8 8-10 3" fill="none" stroke="#c67a4b" stroke-width="3"/></svg>
    <svg class="step-arrow" style="left:708px" width="84" height="30" viewBox="0 0 84 30"><path d="M2 18 Q42 -4 78 18M70 10l8 8-10 3" fill="none" stroke="#c67a4b" stroke-width="3"/></svg>
  </div>
  <div class="steps-cta"><a class="btn" href="#">SCHEDULE APPOINTMENT</a></div>
</section>

<section class="contact">
  <h2 class="msg-title">SEND A MESSAGE</h2>
  <h2 class="info-title">CONTACT</h2>
  <div class="form">
    <div class="form-row"><div class="field">Your Name</div><div class="field">Your Email</div><div class="field">Your Subject</div></div>
    <div class="field area">Message</div>
    <span class="submit">SUBMIT</span>
  </div>
  <div class="info">
    <div><svg width="20" height="24" viewBox="0 0 20 24"><path d="M10 1a8 8 0 0 0-8 8c0 6 8 14 8 14s8-8 8-14a8 8 0 0 0-8-8z" fill="#c67a4b"/><circle cx="10" cy="9" r="3" fill="#3c4955"/></svg><span>Brightvale<br>1420 Meridian Parkway<br>Suite 310<br>Lakeport, TX 75501</span></div>
    <div><svg width="20" height="20" viewBox="0 0 24 24"><circle cx="12" cy="12" r="11" fill="#c67a4b"/><path d="M6 8h12v8H6zM6 8l6 5 6-5" fill="none" stroke="#3c4955" stroke-width="1.6"/></svg><span>mdellow@enterprisebrightvale.example</span></div>
    <div><svg width="20" height="20" viewBox="0 0 24 24"><circle cx="12" cy="12" r="11" fill="#c67a4b"/><path d="M8.5 7l2 2-1.2 1.6a7 7 0 0 0 3.1 3.1L14 12.5l2 2-1.5 2A9 9 0 0 1 7 9z" fill="#3c4955"/></svg><span>(555) 014-0580</span></div>
  </div>
</section>

<footer class="footer">
  <svg class="curve" style="top:-30px" width="1200" height="60" viewBox="0 0 1200 60" preserveAspectRatio="none"><path d="M0 30 Q600 0 1200 30 L1200 60 L0 60Z" fill="#232323"/><path d="M0 30 Q600 0 1200 30" fill="none" stroke="#c67a4b" stroke-width="5"/></svg>
  <div class="footer-brand"><span class="brand-dot"></span><span class="brand-name">BRIGHTVALE</span></div>
  <nav class="footer-links">
    <span><svg width="20" height="18" viewBox="0 0 20 18"><rect x="1" y="3" width="18" height="14" fill="none" stroke="#c67a4b" stroke-width="2"/><path d="M1 7h18M6 1v4M14 1v4" stroke="#c67a4b" stroke-width="2"/></svg>Schedule Appointment</span>
    <span><svg width="18" height="18" viewBox="0 0 24 24"><path d="M6.6 10.8a15 15 0 0 0 6.6 6.6l2.2-2.2a1 1 0 0 1 1-.25 11 11 0 0 0 3.6.6 1 1 0 0 1 1 1V20a1 1 0 0 1-1 1A17 17 0 0 1 3 4a1 1 0 0 1 1-1h3.5a1 1 0 0 1 1 1 11 11 0 0 0 .6 3.6 1 1 0 0 1-.25 1z" fill="#c67a4b"/></svg>Contact Us</span>
  </nav>
</footer>
<section class="copyright">COPYRIGHT © 2018 BRIGHTVALE. ALL RIGHTS RESERVED.</section>

</body>
</html>
```